Australia & New Zealand Sports Flooring, Equipment & Seating Business Needs a Brochure Design

My business "Grandline Athletics" represents Merrow Surfaces from the USA & Tarquin Leisure from Malaysia. I need a new corporate tri fold brochure outlining the general product lines and service offered. Sport is the theme, basketball is a large part of the business with timber floors, rings, nets, backboards and seating followed by athletic equipment for running tracks, soccer goals etc. I have Red, black and white business cards but happy to add other colour/s for effect. Content details available on website www.grandlineathletics.com.au
Updates
Would like the inside pages to be focused on the 3 main product lines, Flooring, Equipment, Seating
new images uploaded if required
Project Deadline Extended
Target Market(s)
Architects, Builders, Stadium Managers, Schools & Universities
Industry/Entity Type
Business
Look and feel
Each slider illustrates characteristics of the customer's brand and the style your logo design should communicate.

```html
<!DOCTYPE html>
<html lang="en">
<head>
<meta charset="utf-8">
<title>Grandline Athletics – Tri-fold Brochure</title>
<link href="https://fonts.googleapis.com/css2?family=Alfa+Slab+One&family=Sorts+Mill+Goudy&family=Cinzel:wght@400&family=Carlito&family=Tinos:wght@400;700&display=swap" rel="stylesheet">
<style>
  :root {
    --red: #ff0000;
    --blue: #0000ff;
    --black: #000000;
    --paper: #ffffff;
    --ink: #1a1a1a;
    --ink-soft: #333333;
    --wood: #c98a4a;
    --wood-dark: #8a5a2e;
    --hall: #3d6b4f;
  }
  * { margin: 0; padding: 0; box-sizing: border-box; }
  html, body { width: 1200px; height: 927px; overflow: hidden; background: var(--paper); }
  .brochure { position: relative; width: 1200px; height: 927px; background: var(--paper); color: var(--ink); }

  .band { position: absolute; top: 0; height: 927px; }
  .band--red { left: 0; width: 143px; background: var(--red); }
  .band--blue { left: 408px; width: 117px; background: var(--blue); }
  .band--black { left: 815px; width: 118px; background: var(--black); }

  .brand-title {
    position: absolute; left: 158px; top: 21px;
    font-family: "Alfa Slab One", serif; font-weight: 400; font-size: 18.5px; color: var(--black); white-space: nowrap;
  }
  .intro {
    position: absolute; left: 147px; top: 72px; width: 250px;
    font-family: "Sorts Mill Goudy", serif; font-size: 15.5px; line-height: 35.7px; color: var(--ink-soft); white-space: nowrap;
  }

  .photo { position: absolute; }
  .photo--court-main { left: 525px; top: 0; width: 268px; height: 409px;
    background: linear-gradient(180deg, #2b4a3a 0%, var(--hall) 30%, #d9d9d2 48%, var(--wood) 62%, var(--wood-dark) 100%); }
  .photo--wheelchair { left: 143px; top: 553px; width: 242px; height: 177px;
    background: linear-gradient(180deg, #5a4a44 0%, var(--wood) 40%, #d49a5c 100%); }
  .photo--maple { left: 934px; top: 593px; width: 266px; height: 192px;
    background: linear-gradient(180deg, #e6e6e6 0%, #9a9aa8 45%, #d8a868 75%, #7a6a5a 100%); }

  .caption { position: absolute; font-family: "Tinos", serif; font-size: 14px; line-height: 17px; color: var(--black); white-space: nowrap; }
  .caption--wheelchair { left: 148px; top: 734px; }
  .caption--court-main { left: 530px; top: 414px; }
  .caption--maple { left: 938px; top: 789px; }

  .contact { position: absolute; left: 530px; top: 461px; width: 275px; font-family: "Sorts Mill Goudy", serif; color: var(--ink-soft); font-size: 13px; white-space: nowrap; }
  .contact__manager { font-family: "Tinos", serif; font-weight: 700; font-size: 13.5px; line-height: 22px; color: var(--black); }
  .contact__address { margin-top: 17px; line-height: 17px; }
  .contact__address--second { margin-top: 16px; }
  .contact__lines { margin-top: 20px; line-height: 17px; }
  .contact__lines .emph { font-family: Arial, Helvetica, sans-serif; font-size: 14px; color: var(--black); }

  .panel-right { position: absolute; left: 938px; top: 44px; width: 258px; }
  .panel-right__name { font-family: "Tinos", serif; font-weight: 700; font-size: 13px; color: var(--black); }
  .panel-right__tagline { margin-top: 24px; font-family: "Cinzel", serif; font-size: 12px; line-height: 19px; color: var(--ink-soft); white-space: nowrap; }
  .panel-right__headline { margin-top: 14px; font-family: "Cinzel", serif; font-weight: 400; font-size: 27px; line-height: 39px; color: var(--black); letter-spacing: 0.5px; white-space: nowrap; }
  .panel-right__products { margin-top: 30px; font-family: "Carlito", sans-serif; font-size: 15.5px; line-height: 20.5px; color: var(--black); width: 258px; }
</style>
</head>
<body>
<main class="brochure">
  <div class="band band--red"></div>
  <div class="band band--blue"></div>
  <div class="band band--black"></div>

  <section class="panel-left">
    <h1 class="brand-title">Grandline Athletics</h1>
    <p class="intro">We partner with architects, builders<br>and schools to make every game<br>day better for players and fans,<br>with real value on every project.<br>Our three product lines cover it all:<br>Flooring – timber and synthetic courts.<br>Equipment – rings, nets, backboards,<br>soccer goals, hurdles and high jump.<br>Seating – bleachers and grandstands.</p>
    <div class="photo photo--wheelchair" role="img" aria-label="Wheelchair basketball players on a timber court by Merrow Surfaces"></div>
    <p class="caption caption--wheelchair">Accessible courts for<br>wheelchair sport.</p>
  </section>

  <section class="panel-middle">
    <div class="photo photo--court-main" role="img" aria-label="Indoor basketball hall with sprung timber floor and green bleachers"></div>
    <p class="caption caption--court-main">Sprung timber flooring<br>and custom bleachers</p>
    <div class="contact">
      <p class="contact__manager">National sales manager: Dale<br>Fenwick</p>
      <p class="contact__address">Primary Business Address: 14 Calder Rd,<br>Kingsbury</p>
      <p class="contact__address contact__address--second">Address 2: Victoria, Australia 3083</p>
      <p class="contact__lines">
        Phone: &nbsp;0400 555 214<br>
        Phone: &nbsp;+61 400 555 214<br>
        Phone: 0400 555 214<br>
        E-mail: <span class="emph">info@grandlineathletics.com.au</span><br>
        <span class="emph">E-mail:</span> dale@grandlineathletics.com.au<br>
        Website URL: http://<br>
        grandlineathletics.sitebuild.com.au/
      </p>
    </div>
  </section>

  <section class="panel-right">
    <p class="panel-right__name">Grandline Athletics</p>
    <p class="panel-right__tagline">WE'RE SURE YOU'LL BE HAPPY<br>WORKING WITH US</p>
    <h2 class="panel-right__headline">We specialize<br>in flooring,<br>equipment and<br>seating but<br>that's not all<br>we do</h2>
    <p class="panel-right__products">Sprung timber NBCA certified floors, portable timber &amp; synthetic courts, WAAC certified athletic gear, rings and backboards, plus custom and retractable seating. All supplied at wholesale.</p>
  </section>
  <div class="photo photo--maple" role="img" aria-label="Gymnasium with maple floor and retractable seating"></div>
  <p class="caption caption--maple">Maple flooring and retractable<br>seating</p>
</main>
</body>
</html>
```